eBook opt in for website

I write short ebooks (2500 words) to give free as an opt in. I need a cover design with block headers within the pages to highlight the specifics sections for PDF.
Book Title:
Bridgeway Mentoring
Sharpen Your Crew Guidance Using Five Simple Habits
I would like to see a design for the front cover that would emphasize a leader's personal growth to team.
The color that comes to mind is blue.
I do have a Brand Design and Icon if you need it.

Leaders with Team Responsibility
Business Consultant

```html
<!DOCTYPE html>
<html lang="en">
<head>
<meta charset="utf-8">
<title>Bridgeway Mentoring – Page 3</title>
<link href="https://fonts.googleapis.com/css2?family=Lato:ital,wght@0,400;0,700;1,400&display=swap" rel="stylesheet">
<style>
  :root {
    --navy: #223a4e;
    --ink: #1e1e1e;
    --rule: #b9bcc0;
    --frame: #d6d8db;
    --paper: #ffffff;
    --highlight: #f4d23c;
  }
  * { box-sizing: border-box; margin: 0; padding: 0; }
  html, body { width: 849px; height: 1200px; overflow: hidden; background: var(--paper); }
  body { font-family: "Lato", sans-serif; color: var(--ink); }
  .page {
    position: relative; width: 849px; height: 1200px;
    background: var(--paper);
  }
  .page-frame {
    position: absolute; inset: 10px;
    border: 2px solid var(--frame);
  }
  .content { position: absolute; left: 52px; right: 52px; top: 30px; }
  p {
    font-size: 21.5px; line-height: 29px; text-align: justify;
  }
  .intro { text-indent: 48px; }
  .rule { height: 2px; background: var(--rule); }
  .rule-top { margin-top: 14px; }
  .section-banner {
    margin: 22px 0 20px; background: var(--navy);
    height: 126px; padding: 7px;
  }
  .section-banner-inner {
    height: 100%; border: 1.5px solid rgba(255,255,255,0.75);
    display: flex; flex-direction: column; justify-content: center; align-items: center;
    color: #fff; font-size: 28px; line-height: 36px;
  }
  .section-banner-inner em { font-style: italic; }
  .strategy-title {
    text-align: center; font-weight: 700; font-size: 21.5px;
    margin: 32px 0 18px;
  }
  .body-text p { margin-bottom: 29px; }
  .body-text p.indent { text-indent: 48px; }
  .footer {
    position: absolute; left: 0; right: 0; top: 1068px;
    text-align: center;
  }
  .author-name {
    display: inline-block; position: relative;
    font-weight: 700; font-size: 26px; letter-spacing: 1px; color: var(--navy);
    padding: 0 6px;
  }
  .author-name::after {
    content: ""; position: absolute; left: 0; right: 0; bottom: 2px; height: 10px;
    background: var(--highlight); z-index: -1;
  }
  .author-role { font-size: 18px; margin-top: 2px; }
  .footer-rule { width: 190px; height: 2px; background: var(--highlight); margin: 8px auto 8px; }
  .author-email { font-size: 14px; }
  .page-number {
    position: absolute; left: 752px; top: 1066px; width: 46px; height: 46px;
    border: 2px solid var(--ink); border-radius: 50%;
    display: flex; align-items: center; justify-content: center;
    font-weight: 700; font-size: 24px;
  }
</style>
</head>
<body>
<div class="page">
  <div class="page-frame"></div>
  <div class="content">
    <p class="intro">In every leader there is an ah-ha moment, like I had, in which you realize you could have had greater success by being a relational leader.</p>
    <div class="rule rule-top"></div>
    <div class="section-banner">
      <div class="section-banner-inner">
        <span>4 Strategies for Developing</span>
        <em>Bridgeway Mentoring</em>
      </div>
    </div>
    <div class="rule"></div>
    <h2 class="strategy-title">Strategy #1: Understanding Your Leadership Style</h2>
    <div class="body-text">
      <p>There are many free tools online to assess your personality and your leadership style. However, the one I have used systematically over the years is Rowan-Ashby. All of my team takes this test when they are hired, including my interns and volunteer staff. It provides a greater understanding of the team as a whole. It also provides the information needed to understand their individual capacity, which used properly can strengthen the team as a whole.</p>
      <p class="indent">Rowan-Ashby (RA) assists you in identifying preferences within your personality. I use the free test on the TypeGrid site. This type of test provides the key to unlock the understanding of a person's very core. This in turn provides optimum performance and a greater engagement for each team member.</p>
      <p>There are 4 Personality Preferences you will read about at TypeGrid Our Theory. The assessment helps you to understand the 4 key elements and how they operate as a whole.</p>
      <p>There are 4 Personality Preferences you will read about at TypeGrid Our Theory. The assessment helps you to understand the 4 key elements and how they operate as a whole.</p>
    </div>
  </div>
  <footer class="footer">
    <div class="author-name">MAREN HOLLOWAY</div>
    <div class="author-role">Bridgeway Mentoring</div>
    <div class="footer-rule"></div>
    <div class="author-email">marenhollowaywrites@mailbox.com</div>
  </footer>
  <div class="page-number">3</div>
</div>
</body>
</html>
```